Design a business card & stationary for a mortgage company

We are looking for a good looking business card design for our mortgage company that includes our logo. We received a free design as part of our logo project but we don't love it. The company is called "Pinecrest Mortgage Company" so we like waves and lighthouses. The logo should be included. We have a version in both vertical and horizontal that we have provided.

Industry/Entity Type

Finance

Contact Information for Business Card

This should include our new logo file

Requirements
Must have
• 3. The details you'd like on the card - name, title, phone, email, website, address, social media handles etc.
1. Marcus Hale
Vice President
732-419-6253
Fax 888-304-2918
mhale@pinecrestmortgage.example
NMLS 47162 - Company NMLS 61290
18 Larkin Ave
Toms River, NJ 08614

```html
<!DOCTYPE html>
<html lang="en">
<head>
<meta charset="utf-8">
<title>Pinecrest Mortgage Company — Stationery</title>
<link rel="stylesheet" href="https://fonts.googleapis.com/css2?family=Sen:wght@400;700&display=swap">
<style>
  :root {
    --backdrop: #a9acb6;
    --paper: #ffffff;
    --navy: #135a92;
    --brand: #1b6aa5;
    --sky: #1f8fdc;
    --ink: #17588f;
    --shadow: 0 6px 18px rgba(40, 44, 60, 0.28);
  }
  * { box-sizing: border-box; margin: 0; padding: 0; }
  html, body { width: 1200px; height: 917px; overflow: hidden; }
  body {
    position: relative;
    background: var(--backdrop);
    font-family: "Sen", "Helvetica Neue", Arial, sans-serif;
    color: var(--ink);
  }
  .icon { width: 16px; height: 16px; fill: var(--sky); flex: none; }

  /* Brand name lockup (text only) */
  .brand-name {
    display: flex; align-items: center; gap: 8px;
    color: var(--brand); font-weight: 700; line-height: 1.05;
    text-transform: uppercase; letter-spacing: 0.02em;
  }
  .brand-name .dot { border-radius: 50%; background: var(--sky); flex: none; }

  /* Letterhead */
  .letterhead {
    position: absolute; left: 84px; top: 54px; width: 622px; height: 804px;
    background: var(--paper); box-shadow: var(--shadow);
  }
  .letterhead .brand-name {
    position: absolute; left: 0; right: 0; top: 18px; justify-content: center;
    font-size: 17px;
  }
  .letterhead .brand-name .dot { width: 14px; height: 14px; }
  .letterhead-footer {
    position: absolute; left: 24px; right: 20px; top: 758px;
    display: flex; justify-content: space-between; align-items: center;
    font-size: 10.5px;
  }
  .contact-item { display: flex; align-items: center; gap: 6px; line-height: 1.25; }
  .letterhead .rule-light { position: absolute; left: 0; right: 0; top: 788px; height: 4px; background: var(--sky); }
  .letterhead .rule-dark { position: absolute; left: 0; right: 0; top: 792px; height: 12px; background: var(--navy); }

  /* Business card front */
  .card-front {
    position: absolute; left: 730px; top: 214px; width: 429px; height: 246px;
    background: var(--paper); box-shadow: var(--shadow); overflow: hidden;
  }
  .card-front .rule-top { position: absolute; left: 0; right: 0; top: 0; height: 7px; background: var(--sky); }
  .card-front .rule-light { position: absolute; left: 0; right: 0; top: 218px; height: 4px; background: var(--sky); }
  .card-front .rule-dark { position: absolute; left: 0; right: 0; top: 222px; height: 24px; background: var(--navy); }
  .card-front .brand-name { position: absolute; left: 23px; top: 44px; font-size: 16px; }
  .card-front .brand-name .dot { width: 13px; height: 13px; }
  .card-contacts {
    position: absolute; left: 24px; top: 120px; list-style: none;
    display: flex; flex-direction: column; gap: 3px; font-size: 9.5px;
  }
  .card-contacts .icon { width: 14px; height: 14px; }
  .holder { position: absolute; right: 28px; top: 132px; width: 160px; text-align: center; }
  .holder-name { font-size: 18px; font-weight: 700; color: var(--brand); }
  .holder-title { font-size: 13.5px; color: var(--sky); margin-top: 2px; }

  /* Business card back */
  .card-back {
    position: absolute; left: 730px; top: 505px; width: 431px; height: 247px;
    background: var(--navy); box-shadow: var(--shadow); color: #fff;
  }
  .card-back .brand-name {
    position: absolute; left: 0; right: 0; top: 82px; justify-content: center;
    color: #fff; font-size: 20px;
  }
  .card-back .brand-name .dot { width: 16px; height: 16px; background: #fff; }
  .licence { position: absolute; left: 0; right: 0; top: 161px; text-align: center; font-size: 11.5px; letter-spacing: 0.02em; }
</style>
</head>
<body>
<svg width="0" height="0" style="position:absolute" aria-hidden="true">
  <defs>
    <symbol id="i-pin" viewBox="0 0 16 16"><path d="M8 1a5 5 0 0 0-5 5c0 3.6 5 8.5 5 8.5S13 9.6 13 6a5 5 0 0 0-5-5zm0 7a2 2 0 1 1 0-4 2 2 0 0 1 0 4z"/></symbol>
    <symbol id="i-phone" viewBox="0 0 16 16"><path d="M4.2 1.5l2 2.8-1.3 1.5c.8 2 2.3 3.6 4.3 4.5l1.5-1.3 2.8 2-1 2.3C7.5 13.6 2.4 8.5 2 3.3z"/></symbol>
    <symbol id="i-fax" viewBox="0 0 16 16"><path d="M5 1h6v4H5zM2 5h12v10H2zm2 2v2h8V7zm1 4h1.5v1.3H5zm2.8 0h1.5v1.3H7.8zm2.7 0H12v1.3h-1.5zM5 13h1.5v1H5zm2.8 0h1.5v1H7.8zm2.7 0H12v1h-1.5z" fill-rule="evenodd"/></symbol>
    <symbol id="i-mail" viewBox="0 0 16 16"><path d="M1 3.5h14v9H1zm1.3 1L8 9l5.7-4.5z" fill-rule="evenodd"/></symbol>
  </defs>
</svg>

<section class="letterhead" aria-label="Letterhead">
  <div class="brand-name"><span class="dot"></span><span>Pinecrest<br>Mortgage Company</span></div>
  <footer class="letterhead-footer">
    <div class="contact-item"><svg class="icon"><use href="#i-pin"/></svg><span>18 Larkin Ave<br>Toms River, NJ 08614</span></div>
    <div class="contact-item"><svg class="icon"><use href="#i-phone"/></svg><span>732-419-6253</span></div>
    <div class="contact-item"><svg class="icon"><use href="#i-fax"/></svg><span>888-304-2918</span></div>
    <div class="contact-item"><svg class="icon"><use href="#i-mail"/></svg><span>mhale@pinecrestmortgage.example</span></div>
  </footer>
  <div class="rule-light"></div>
  <div class="rule-dark"></div>
</section>

<section class="card-front" aria-label="Business card front">
  <div class="rule-top"></div>
  <div class="brand-name"><span class="dot"></span><span>Pinecrest<br>Mortgage Company</span></div>
  <ul class="card-contacts">
    <li class="contact-item"><svg class="icon"><use href="#i-pin"/></svg><span>18 Larkin Ave Toms River, NJ 08614</span></li>
    <li class="contact-item"><svg class="icon"><use href="#i-fax"/></svg><span>888-304-2918</span></li>
    <li class="contact-item"><svg class="icon"><use href="#i-phone"/></svg><span>732-419-6253</span></li>
    <li class="contact-item"><svg class="icon"><use href="#i-mail"/></svg><span>mhale@pinecrestmortgage.example</span></li>
  </ul>
  <div class="holder">
    <div class="holder-name">Marcus Hale</div>
    <div class="holder-title">Vice President</div>
  </div>
  <div class="rule-light"></div>
  <div class="rule-dark"></div>
</section>

<section class="card-back" aria-label="Business card back">
  <div class="brand-name"><span class="dot"></span><span>Pinecrest<br>Mortgage Company</span></div>
  <p class="licence">NMLS 47162 - Company NMLS 61290</p>
</section>
</body>
</html>
```